Geschäftspapiere Campingplatz
Zielgruppe
Campingplatz
Aufgabenstellung
Geschäftspapiere, Briefpapier, Visitenkarte, Briefumschlag und DIN A5 Memoblock farblich und designmäßig am Logo orientiert.
Memoblock sollte sich vom Briefpapier unterscheiden und nicht so viele Daten enthalten.
Website, E-Mail, Telefonnummer, Festnetz, Adresse und Inhaber sollen auf dem Briefpapier erscheinen.
Auf der Visitenkarte soll nur statt Inhaber stehen und zusätzlich die Handynummer, sowie alle anderen Daten.
Die Datensätze sollten sich mit entsprechendem Programm von uns bearbeiten lassen.

```html
<!DOCTYPE html>
<html lang="de">
<head>
<meta charset="utf-8">
<title>Geschäftspapiere Camping Lindgrün</title>
<link href="https://fonts.googleapis.com/css2?family=Source+Sans+3:wght@300;400;600&display=swap" rel="stylesheet">
<style>
  :root {
    --stage: #1e3a5c;
    --paper: #ffffff;
    --green: #7aa33c;
    --green-light: #a3c274;
    --ink: #3a3a3a;
    --muted: #8a8a8a;
  }
  * { box-sizing: border-box; margin: 0; padding: 0; }
  html, body { width: 1200px; height: 800px; overflow: hidden; }
  body {
    background: var(--stage);
    font-family: "Source Sans 3", sans-serif;
    color: var(--ink);
    position: relative;
  }
  .sheet { position: absolute; background: var(--paper); overflow: hidden; }
  .brand-name {
    color: var(--green);
    font-weight: 600;
    display: flex; align-items: center; gap: 6px;
    white-space: nowrap;
  }
  .brand-dot { border-radius: 50%; background: var(--green); display: inline-block; }
  .rule { position: absolute; height: 1px; background: var(--green); }

  /* Letterhead */
  .letterhead { left: 50px; top: 70px; width: 340px; height: 480px; }
  .letterhead .brand-name { position: absolute; left: 28px; top: 26px; font-size: 15px; }
  .letterhead .brand-dot { width: 10px; height: 10px; }
  .letterhead .rule { left: 28px; right: 28px; top: 52px; }
  .letter-body { position: absolute; left: 28px; right: 40px; top: 110px; font-size: 7.5px; line-height: 1.55; color: #555; }
  .letter-body p { margin-bottom: 8px; }
  .footer-band {
    position: absolute; left: 0; right: 0; bottom: 0; height: 56px;
    background: var(--green); color: var(--paper);
    display: flex; justify-content: space-between; align-items: center;
    padding: 0 28px; font-size: 7.5px; line-height: 1.5;
  }
  .footer-band .contact { text-align: right; }
  .footer-band strong { font-weight: 600; }

  /* Envelope */
  .envelope { position: absolute; left: 430px; top: 50px; width: 400px; height: 250px; }

  /* Memo pad */
  .memo { left: 430px; top: 330px; width: 400px; height: 283px; }
  .memo .brand-name { position: absolute; left: 24px; top: 22px; font-size: 13px; }
  .memo .brand-dot { width: 8px; height: 8px; }
  .memo .rule { left: 24px; right: 24px; top: 44px; }
  .memo .footer-band { height: 42px; padding: 0 24px; font-size: 7px; }

  /* Business cards */
  .card { width: 260px; height: 168px; left: 880px; }
  .card-front { top: 330px; display: flex; flex-direction: column; align-items: center; justify-content: center; gap: 8px; }
  .card-front .brand-name { font-size: 19px; }
  .card-front .brand-dot { width: 12px; height: 12px; }
  .card-front .rule { position: static; width: 150px; }
  .card-back { top: 520px; }
  .card-back .holder { position: absolute; left: 18px; top: 16px; }
  .card-back .holder-name { font-size: 17px; font-weight: 300; letter-spacing: 0.5px; color: var(--muted); }
  .card-back .holder-name strong { font-weight: 600; color: var(--ink); }
  .card-back .holder-role { font-size: 7px; color: var(--muted); letter-spacing: 1px; text-transform: uppercase; }
  .card-back .info-band {
    position: absolute; left: 0; right: 0; bottom: 0; height: 100px;
    background: var(--green); color: var(--paper);
    display: grid; grid-template-columns: repeat(3, 1fr);
    padding: 12px 10px; gap: 6px; text-align: center; font-size: 7px; line-height: 1.45;
  }
  .info-icon {
    width: 28px; height: 28px; margin: 0 auto 6px;
    border: 1px dashed rgba(255,255,255,0.7); border-radius: 50%;
    display: flex; align-items: center; justify-content: center;
  }
</style>
</head>
<body>

  <section class="sheet letterhead" aria-label="Briefpapier">
    <div class="brand-name"><span class="brand-dot"></span>Camping Lindgrün</div>
    <div class="rule"></div>
    <div class="letter-body">
      <p>Sehr geehrte Damen und Herren,</p>
      <p>vielen Dank für Ihre Anfrage zu unserem Campingplatz. Gerne bestätigen wir Ihre Reservierung für den gewünschten Zeitraum und freuen uns auf Ihren Besuch bei uns im Tal.</p>
      <p>Mit freundlichen Grüßen</p>
    </div>
    <div class="footer-band">
      <div class="address"><strong>Camping Lindgrün</strong><br>Fam. Brandauer<br>Waldweg 12<br>54321 Tannenau</div>
      <div class="contact">info@camping-lindgruen.de<br>www.camping-lindgruen.de<br>Telefon: +49 1234 567890<br>Telefax: +49 1234 567891</div>
    </div>
  </section>

  <svg class="envelope" viewBox="0 0 400 250" role="group" aria-label="Briefumschlag">
    <polygon points="20,0 380,0 400,70 0,70" fill="var(--green-light)"/>
    <rect x="0" y="70" width="400" height="180" fill="var(--paper)"/>
    <polygon points="0,70 400,70 360,120 40,120" fill="var(--green)"/>
  </svg>

  <section class="sheet memo" aria-label="Memoblock">
    <div class="brand-name"><span class="brand-dot"></span>Camping Lindgrün</div>
    <div class="rule"></div>
    <div class="footer-band">
      <div class="address"><strong>Camping Lindgrün</strong><br>Waldweg 12 · 54321 Tannenau</div>
      <div class="contact">info@camping-lindgruen.de<br>Telefon: +49 1234 567890</div>
    </div>
  </section>

  <section class="sheet card card-front" aria-label="Visitenkarte Vorderseite">
    <div class="brand-name"><span class="brand-dot"></span>Camping Lindgrün</div>
    <div class="rule"></div>
  </section>

  <section class="sheet card card-back" aria-label="Visitenkarte Rückseite">
    <div class="holder">
      <div class="holder-name">FAM. <strong>BRANDAUER</strong></div>
      <div class="holder-role">Camping Lindgrün</div>
    </div>
    <div class="info-band">
      <div>
        <div class="info-icon">
          <svg width="12" height="14" viewBox="0 0 12 14"><path d="M6 0a5 5 0 0 0-5 5c0 4 5 9 5 9s5-5 5-9a5 5 0 0 0-5-5zm0 7a2 2 0 1 1 0-4 2 2 0 0 1 0 4z" fill="#fff"/></svg>
        </div>
        Waldweg 12<br>54321 Tannenau
      </div>
      <div>
        <div class="info-icon">
          <svg width="14" height="12" viewBox="0 0 14 12"><path d="M1 4c0-2 2-3 6-3s6 1 6 3v1h-3V3.5H4V5H1zM3 6h8l1.5 5h-11z" fill="#fff"/></svg>
        </div>
        +49 1234 567890<br>+49 1234 567891<br>Mobil: +49 170 1234567
      </div>
      <div>
        <div class="info-icon">
          <svg width="13" height="13" viewBox="0 0 14 14" fill="none" stroke="#fff" stroke-width="1.2"><circle cx="7" cy="7" r="6"/><ellipse cx="7" cy="7" rx="2.6" ry="6"/><path d="M1 7h12"/></svg>
        </div>
        info@camping-lindgruen.de<br>www.camping-lindgruen.de
      </div>
    </div>
  </section>

</body>
</html>
```